VORN Paradigm. the way you communicate in every situation and in all environments.

I would like you to create a diagram depicting a very specific process of communication. it must follow the look of the diagram that i have attached. this is going to be used in a book called LANTERN. it is going to explain the fact that we communicate all the same way using this process as we communicate. it starts with the fact that everyone takes everything that is said personally and then moves on to filters, which is your own agenda or experience kicking in. then you move to your why it matters, which is your motivation and ends with the choice of words you use when you communicate. if you are going to be successful then you must separate the person from the issue.

Target Market(s)

market is executive business people around the world

Industry/Entity Type

Consulting

Font styles to use
Sans Serif

Colors

Designer to choose only greyscale colors for use in the design.

Requirements
Must have
• I would like it to have a diving/ocean/snorkel feel to it. The analogy we are using is to make a deep dive when you are communicating. it must have every part of the diagram you see, it starts at the top with the vorn paradigm (and the words) it then connects to the filters which connects to the why it matters with connects to the words and then end with the separating the person from the issue.
Nice to have
• we are writing a black and white book NO color. therefore the words should be clear and easy to read. Each section should be able to stand on its own so we can write about it separately.
Should not have
• the diagram DOES NOT have to look like the one i gave you. it must explain the fact that it starts with VORN and ends with Separate and must pass through the three areas to get to the SEPARATE.

```html
<!DOCTYPE html>
<html lang="en">
<head>
<meta charset="utf-8">
<title>VORN Paradigm – Communication Process</title>
<link rel="stylesheet" href="https://fonts.googleapis.com/css2?family=Arimo:wght@400;700&display=swap">
<style>
  :root {
    --sea-surface: #d9d9d9;
    --sea-mid: #c2c2c2;
    --sea-deep: #a3a3a3;
    --seabed: #8f8f8f;
    --wave: #f4f4f4;
    --bubble: #fafafa;
    --gauge: #7a7a7a;
    --flow: #767676;
    --ring-light: #f2f2f2;
    --ring-dark: #d0d0d0;
    --face-top: #ffffff;
    --face-bottom: #ebebeb;
    --title: #353535;
    --body: #1c1c1c;
  }
  html, body {
    margin: 0;
    padding: 0;
    width: 1200px;
    height: 1200px;
    overflow: hidden;
    background: var(--sea-mid);
  }
  .diagram {
    display: block;
    width: 1200px;
    height: 1200px;
    font-family: "Arimo", Arial, sans-serif;
  }
  .sea-wave {
    fill: none;
    stroke: var(--wave);
    stroke-linecap: round;
  }
  .sea-wave--main { stroke-width: 8; opacity: 0.9; }
  .sea-wave--soft { stroke-width: 5; opacity: 0.5; }
  .bubble {
    fill: none;
    stroke: var(--bubble);
    stroke-width: 4;
    opacity: 0.75;
  }
  .bubble--small { stroke-width: 3; opacity: 0.6; }
  .depth-gauge line {
    stroke: var(--gauge);
    stroke-width: 4;
    stroke-linecap: round;
  }
  .depth-gauge .tick--major { stroke-width: 6; }
  .seabed { fill: var(--seabed); opacity: 0.55; }
  .flow-line {
    fill: none;
    stroke: var(--flow);
    stroke-width: 22;
    stroke-linecap: round;
  }
  .flow-head { fill: var(--flow); }
  .node-ring { fill: url(#ringGrad); }
  .node-face { fill: url(#faceGrad); }
  .node-title {
    fill: var(--title);
    font-weight: 700;
    font-size: 48px;
    text-anchor: middle;
  }
  .node-body {
    fill: var(--body);
    font-weight: 400;
    font-size: 40px;
    text-anchor: middle;
  }
  .node-body--compact { font-size: 39px; }
</style>
</head>
<body>
<svg class="diagram" viewBox="0 0 1800 1800" xmlns="http://www.w3.org/2000/svg" role="img" aria-label="VORN Paradigm communication process, a deep dive: VORN Paradigm, Your Filters, Why It Matters, Your Words, What To Do">
  <defs>
    <linearGradient id="seaGrad" x1="0" y1="0" x2="0" y2="1">
      <stop offset="0" stop-color="var(--sea-surface)"/>
      <stop offset="0.45" stop-color="var(--sea-mid)"/>
      <stop offset="1" stop-color="var(--sea-deep)"/>
    </linearGradient>
    <linearGradient id="ringGrad" x1="0" y1="0" x2="1" y2="1">
      <stop offset="0" stop-color="var(--ring-light)"/>
      <stop offset="1" stop-color="var(--ring-dark)"/>
    </linearGradient>
    <linearGradient id="faceGrad" x1="0" y1="0" x2="0" y2="1">
      <stop offset="0" stop-color="var(--face-top)"/>
      <stop offset="0.6" stop-color="#f7f7f7"/>
      <stop offset="1" stop-color="var(--face-bottom)"/>
    </linearGradient>
  </defs>

  <!-- Water: depth gradient, surface waves, seabed -->
  <g class="sea">
    <rect x="0" y="0" width="1800" height="1800" fill="url(#seaGrad)"/>
    <path class="sea-wave sea-wave--main" d="M0 90 Q75 60 150 90 T300 90 T450 90 T600 90 T750 90 T900 90 T1050 90 T1200 90 T1350 90 T1500 90 T1650 90 T1800 90"/>
    <path class="sea-wave sea-wave--soft" d="M0 135 Q75 110 150 135 T300 135 T450 135 T600 135 T750 135 T900 135 T1050 135 T1200 135 T1350 135 T1500 135 T1650 135 T1800 135"/>
    <path class="seabed" d="M0 1720 Q300 1670 600 1710 T1200 1700 T1800 1690 L1800 1800 L0 1800 Z"/>
  </g>

  <!-- Depth gauge -->
  <g class="depth-gauge">
    <line x1="1730" y1="220" x2="1730" y2="1620"/>
    <line class="tick--major" x1="1700" y1="220" x2="1760" y2="220"/>
    <line x1="1712" y1="395" x2="1748" y2="395"/>
    <line class="tick--major" x1="1700" y1="570" x2="1760" y2="570"/>
    <line x1="1712" y1="745" x2="1748" y2="745"/>
    <line class="tick--major" x1="1700" y1="920" x2="1760" y2="920"/>
    <line x1="1712" y1="1095" x2="1748" y2="1095"/>
    <line class="tick--major" x1="1700" y1="1270" x2="1760" y2="1270"/>
    <line x1="1712" y1="1445" x2="1748" y2="1445"/>
    <line class="tick--major" x1="1700" y1="1620" x2="1760" y2="1620"/>
  </g>

  <!-- Rising bubbles -->
  <g class="bubbles">
    <circle class="bubble" cx="420" cy="470" r="22"/>
    <circle class="bubble bubble--small" cx="470" cy="380" r="13"/>
    <circle class="bubble bubble--small" cx="440" cy="300" r="9"/>
    <circle class="bubble" cx="1320" cy="470" r="18"/>
    <circle class="bubble bubble--small" cx="1370" cy="390" r="11"/>
    <circle class="bubble bubble--small" cx="1345" cy="320" r="7"/>
    <circle class="bubble" cx="1330" cy="1500" r="24"/>
    <circle class="bubble bubble--small" cx="1390" cy="1400" r="14"/>
    <circle class="bubble bubble--small" cx="1360" cy="1320" r="9"/>
    <circle class="bubble" cx="420" cy="1480" r="20"/>
    <circle class="bubble bubble--small" cx="470" cy="1390" r="12"/>
    <circle class="bubble bubble--small" cx="445" cy="1310" r="8"/>
  </g>

  <!-- Flow paths -->
  <g class="flow">
    <path class="flow-line" d="M905 200 A232 232 0 0 1 925 663"/>
    <path class="flow-line" d="M905 665 L385 665"/>
    <path class="flow-line" d="M350 665 A235 235 0 0 0 330 1134"/>
    <path class="flow-line" d="M380 1133 A215 215 0 0 0 592 950"/>
    <path class="flow-line" d="M592 918 A213 213 0 0 1 775 705"/>
    <path class="flow-line" d="M1005 1095 A212 212 0 0 0 1217 915"/>
    <path class="flow-line" d="M1217 885 A212 212 0 0 1 1400 670"/>
    <path class="flow-line" d="M1455 665 A235 235 0 0 1 1490 1133"/>
    <path class="flow-line" d="M1465 1133 L935 1133"/>
    <path class="flow-line" d="M905 1133 A232 232 0 0 0 905 1597"/>

    <polygon class="flow-head" points="912,660 950,636 950,686"/>
    <polygon class="flow-head" points="358,665 398,642 398,688"/>
    <polygon class="flow-head" points="350,1134 305,1111 305,1156"/>
    <polygon class="flow-head" points="592,932 568,968 614,968"/>
    <polygon class="flow-head" points="806,705 762,682 770,728"/>
    <polygon class="flow-head" points="1217,884 1194,925 1240,925"/>
    <polygon class="flow-head" points="1430,668 1385,648 1390,694"/>
    <polygon class="flow-head" points="1468,1133 1505,1110 1505,1156"/>
    <polygon class="flow-head" points="910,1133 950,1110 950,1156"/>
  </g>

  <!-- Stage: VORN Paradigm -->
  <g class="node node--start">
    <circle class="node-ring" cx="905" cy="432" r="197"/>
    <circle class="node-face" cx="905" cy="432" r="180"/>
    <text class="node-title" x="905" y="325">VORN</text>
    <text class="node-title" x="905" y="375">Paradigm</text>
    <text class="node-body" x="908" y="434">When words are</text>
    <text class="node-body" x="908" y="484">taken personally,</text>
    <text class="node-body" x="908" y="533">what happens?</text>
  </g>

  <!-- Stage: Your Filters -->
  <g class="node node--filters">
    <circle class="node-ring" cx="350" cy="900" r="197"/>
    <circle class="node-face" cx="350" cy="900" r="180"/>
    <text class="node-title" x="352" y="778">Your</text>
    <text class="node-title" x="352" y="828">Filters</text>
    <text class="node-body" x="350" y="884">An accumulation</text>
    <text class="node-body" x="350" y="934">of your experience,</text>
    <text class="node-body" x="350" y="984">knowledge and</text>
    <text class="node-body" x="350" y="1034">values</text>
  </g>

  <!-- Stage: Why It Matters -->
  <g class="node node--motive">
    <circle class="node-ring" cx="905" cy="900" r="197"/>
    <circle class="node-face" cx="905" cy="900" r="180"/>
    <text class="node-title" x="905" y="777">Why It</text>
    <text class="node-title" x="905" y="827">Matters</text>
    <text class="node-body" x="905" y="874">This is your</text>
    <text class="node-body" x="905" y="920">compass. It is what</text>
    <text class="node-body" x="905" y="966">motivates you,</text>
    <text class="node-body" x="905" y="1012">what drives</text>
    <text class="node-body" x="905" y="1058">you.</text>
  </g>

  <!-- Stage: Your Words -->
  <g class="node node--words">
    <circle class="node-ring" cx="1465" cy="900" r="197"/>
    <circle class="node-face" cx="1465" cy="900" r="180"/>
    <text class="node-title" x="1465" y="773">Your</text>
    <text class="node-title" x="1465" y="823">Words</text>
    <text class="node-body node-body--compact" x="1462" y="871">This is your</text>
    <text class="node-body node-body--compact" x="1462" y="915">immediate</text>
    <text class="node-body node-body--compact" x="1462" y="959">response, verbal</text>
    <text class="node-body node-body--compact" x="1462" y="1003">or perhaps</text>
    <text class="node-body node-body--compact" x="1462" y="1046">non-verbal.</text>
  </g>

  <!-- Stage: What To Do -->
  <g class="node node--end">
    <circle class="node-ring" cx="905" cy="1365" r="197"/>
    <circle class="node-face" cx="905" cy="1365" r="180"/>
    <text class="node-title" x="907" y="1258">What</text>
    <text class="node-title" x="907" y="1308">To Do</text>
    <text class="node-body" x="896" y="1362">Separate the</text>
    <text class="node-body" x="896" y="1412">Person from the</text>
    <text class="node-body" x="896" y="1462">Issue</text>
  </g>
</svg>
</body>
</html>
```